Sitecraft website build: Quill literary annual (initial design work supplied)

Our brand guidelines provide the look and feel for the website - we just need someone to create it based on our mock ups!
PLEASE NOTE:
- Please base our website off the website pages within the brief (ie homepage is GREEN)
- please ensure each page will be standalone (not a scrolling home page)
- please only use filtered duotone style photography as a hold, if you think the page needs a photo.
-please not the websites i have provided as an influence - especially BRINE ANNUAL. We want very little photography.

Quill is a literary and arts journal that provides a platform for both emerging and established writers and artists from New Zealand and beyond. We are passionate about sharing insights into the intimate and unique worlds of creatives with short stories, poetry, and art – showcasing raw and unfiltered glimpses into their world.

We have our brand guidelines and logo finalised, with a 'look and feel' design for the website within our attached brand guidelines document. We just need someone to design this simple website on Sitecraft for us. It will have five pages and will need a newsletter sign up link:
Home page
About us page
Submissions page
Purchase page
Contact page

DRAFT WEB COPY

ABOUT
QUILL is an independent literary annual journal established in 2022 by Harriet Calloway and Mereana Platt that publishes unrepentant unfiltered accounts of life, eclectic takes on the mundane ordinary, and deep dives into modern love & sexuality.
Founder, Editor: Harriet Anahera Calloway
Founder, Production Director: Mereana Platt
Art Direction: Corin Ashby
Editorial Assistant: Lucy Fenwick-Dorsey

I suggest duotone fashion-esque photography which is very Marla Quiggin/ Palm Springs vibe but not obviously identifiable.
· I love the style of Rex Havelin for our shoot in particular. Group lazing around a pool, leisurely, glam, but effortless and ironically looking very natural – as though – yes, these are our lives.
SUBMISSION PAGE
Quill welcomes submissions all year round.
We are drawn to dark humour, satirical takes on the social scene, and starkly honest accounts of ordinary life. Diversity is celebrated, adversity is welcomed and, above all, personal expression is championed. We are particularly seeking content that takes risks, screams of honesty and celebrates life’s most extraordinary moments.
Selected works will be published in our annual publication.

Submission guidelines
We accept flash fiction, short stories and poetry. Individual entries not to mustn’t exceed 2000 words.
Submitted work must be unpublished and in English. We welcome simultaneous submissions, but must be notified immediately if your manuscript is accepted for publication elsewhere or appears in any print or online source. We will endeavour to respond to all submissions within four weeks.
Please send submissions as a word document along with a brief bio of 50 words to inkwell@quilljournal.example
PO Box[EB2]
​Note on Copyright: Copyright remains with the author.

Annual short story competition
Issue One is interested in all that is spiritual, coincidental, or mysterious. Stories selected for this issue reflect life’s uncanny moments, those that defy explanation, and experiences that promote personal and spiritual growth. Entires must be no longer than 2000 words.

First prize: 1000
Second prize: 500
Third prize: 200[EB3]

SUPPORT US
Since our launch in 2022, we have relied upon the generous support of our creative business community in Wellington City, New Zealand. If you read us, or love our ethos, please consider a donation.
Link to chipinhere page
Updates

Hello designers
I would ideally love to have someone turn this around within a few weeks, because the design work has mostly been provided.
Thanks
Harriet

Hi everyone Please ensure you read our brand guidelines and follow the brief. Please note we do not yet have a product, as this is a new venture, so there is no point including images of a magazine that doesn't yet exist. Some further comment to ensure we get there: - We want all pages to be separate pages (not a scrolling home page) with a different colour based on the guidelines - The home page must look just as it does in the brand guidelines - There is no archive page (please read brief) as we have no archive yet. The pages are: Home, About, Contact, Competitions and submissions Thank you

Target Market(s)

writers and creatives

Industry/Entity Type

Writing/ creative/ publishing

Coding

Coded - Design and coding required

Number of Pages Required

4 page

Font styles to use
Other font styles liked:
• COTTA and Univers - as per brand guidelines

Requirements
Must have
• Sitecraft designer needed to design our mocked up webpages.
Nice to have
• As close to the brand guideline mock ups as possible (see page 11,12,13)
Should not have
• anything outside of the brand guidelines

```html
<!DOCTYPE html>
<html lang="en">
<head>
<meta charset="utf-8">
<title>Quill — a literary and arts journal</title>
<link href="https://fonts.googleapis.com/css2?family=Cormorant+Garamond:wght@400;500&family=Oswald:wght@300;400&family=Inter:wght@400;700&display=swap" rel="stylesheet">
<style>
:root{
  --plum:#5e2753;
  --plum-deep:#4a1d43;
  --rose:#c4506f;
  --blush:#fcf0f4;
  --blush-2:#f8e4ec;
  --ink:#3b3340;
  --muted:#7c7480;
  --white:#ffffff;
  --serif:'Cormorant Garamond', serif;
  --cond:'Oswald', sans-serif;
  --sans:'Inter', sans-serif;
}
*{box-sizing:border-box;margin:0;padding:0}
html,body{width:1200px;height:4918px;overflow:hidden;background:var(--white)}
body{font-family:var(--sans);color:var(--ink)}
.page{position:relative;width:1200px;height:4918px;overflow:hidden}
.abs{position:absolute}
.block{position:absolute;display:block}
a{color:inherit;text-decoration:none}

/* header */
.brand{position:absolute;left:86px;top:4px;font-family:var(--serif);font-weight:500;font-size:88px;line-height:1;color:var(--plum);letter-spacing:-1px}
.nav{position:absolute;left:414px;top:52px;display:flex;gap:0;font-family:var(--cond);font-weight:300;font-size:17px;color:var(--plum);letter-spacing:.5px}
.nav a{padding:0 18px;border-left:1px solid var(--plum);line-height:20px}
.nav a:first-child{border-left:none;padding-left:0}
.social-top{position:absolute;left:1000px;top:56px;display:flex;gap:14px;font-family:var(--sans);font-size:12px;color:var(--ink)}

/* hero */
.hero-bg{left:0;top:128px;width:1200px;height:599px;background:var(--blush)}
.photo-tower{left:0;top:128px;width:525px;height:599px;background:linear-gradient(135deg,#3a1238,#6b2a62 60%,#4b1845)}
.photo-arches{left:254px;top:183px;width:359px;height:489px;background:linear-gradient(180deg,#d2577a,#c0456d 55%,#a73a5f)}
.hero-title{left:536px;top:244px;width:600px;font-family:var(--serif);font-size:49px;line-height:53px;color:var(--plum);font-weight:400}
.hero-text{left:672px;top:430px;width:450px;font-size:17px;line-height:26px;color:var(--ink)}
.btn{position:absolute;display:flex;align-items:center;justify-content:center;border:1.5px solid var(--plum);border-radius:30px;font-family:var(--cond);font-weight:400;font-size:18px;color:var(--plum);letter-spacing:.5px}
.btn--rose{border-color:var(--rose);color:var(--rose)}

/* competition */
.comp-bg{left:0;top:727px;width:1200px;height:319px;background:var(--blush)}
.section-title{position:absolute;font-family:var(--serif);font-weight:400;color:var(--plum);line-height:1.15}
.centered{left:0;width:1200px;text-align:center}
.comp-text{left:197px;top:850px;width:814px;text-align:center;font-size:14px;line-height:22px;color:var(--muted)}
.prize{position:absolute;top:945px;display:flex;gap:12px;align-items:flex-start;font-size:14px;line-height:22px;color:var(--muted)}
.prize strong{display:block;color:var(--ink);font-weight:700;font-size:13px}

/* about */
.photo-leaves{left:767px;top:1046px;width:433px;height:553px;background:linear-gradient(150deg,#1b1f1a,#3a2f3a 50%,#232a22)}
.photo-portrait{left:645px;top:1183px;width:360px;height:462px;background:linear-gradient(180deg,#6b3a63,#542a4e);outline:10px solid var(--white)}
.about-text{left:86px;top:1312px;width:480px;font-size:14.5px;line-height:23px;color:var(--muted)}
.credit{position:absolute;left:86px;font-size:16px;color:var(--ink)}
.credit b{font-weight:700}

/* support */
.photo-frame-leaf{left:0;top:1807px;width:410px;height:536px;background:linear-gradient(160deg,#ef7fa8,#e86f9a 50%,#2a3b2c 80%)}
.photo-hand{left:279px;top:1893px;width:305px;height:362px;background:linear-gradient(170deg,#f8a8e4,#f6b2e0 55%,#a9d9f0)}
.body-copy{position:absolute;font-size:14.5px;line-height:23px;color:var(--muted)}

/* submissions */
.subm-bg{left:0;top:2343px;width:601px;height:561px;background:var(--blush)}
.photo-monstera{left:601px;top:2343px;width:599px;height:561px;background:linear-gradient(135deg,#1a0f5a,#8a1ec8 45%,#d12ad8 70%,#150c40)}

/* magazines */
.mag-band{left:0;top:3545px;width:1200px;height:1005px;background:var(--blush)}
.card{position:absolute;top:3154px;width:237px;height:566px;background:var(--white);box-shadow:0 4px 18px rgba(80,30,70,.12)}
.card-head{position:absolute;left:0;top:0;width:237px;height:328px}
.card-meta{position:absolute;top:22px;left:0;width:100%;display:flex;justify-content:space-between;align-items:center;padding:0 16px;font-family:var(--cond);font-size:11px}
.card-logo{font-family:var(--serif);font-weight:500;font-size:40px;line-height:1}
.card-img{position:absolute;left:24px;top:90px;width:189px;height:238px}
.card-title{position:absolute;top:348px;width:100%;text-align:center;font-family:var(--cond);font-size:19px;color:var(--ink)}
.card-text{position:absolute;top:384px;left:20px;width:197px;text-align:center;font-size:12px;line-height:20px;color:var(--muted)}
.card .btn{top:478px;left:52px;width:133px;height:40px;border-color:var(--ink);color:var(--ink);font-size:12px}
.dots{position:absolute;left:552px;top:3770px;display:flex;gap:14px}
.dots span{width:11px;height:11px;background:#ecc7d5}
.dots span:first-child{background:var(--plum)}

/* newsletter */
.photo-blossom{left:86px;top:4016px;width:587px;height:420px;background:linear-gradient(160deg,#e8c9ef,#d9b2e8 55%,#b8e6ec)}
.news-card{left:471px;top:4092px;width:643px;height:268px;background:var(--white);box-shadow:0 4px 18px rgba(80,30,70,.1)}
.input{position:absolute;left:519px;top:4232px;width:362px;height:47px;background:#e9e1e5;font-size:12px;color:var(--muted);padding:15px 22px}
.btn-solid{position:absolute;left:897px;top:4232px;width:139px;height:47px;border-radius:30px;background:var(--plum);color:var(--white);font-family:var(--cond);font-size:17px;display:flex;align-items:center;justify-content:center}

/* footer */
.footer-bg{left:0;top:4550px;width:1200px;height:368px;background:var(--white)}
.foot-title{position:absolute;font-family:var(--serif);font-size:23px;color:var(--ink)}
.foot-links{position:absolute;font-size:14px;line-height:38px;color:var(--muted)}
.foot-links--u a{text-decoration:underline;color:var(--ink)}
.foot-brand{position:absolute;left:958px;top:4610px;font-family:var(--serif);font-weight:500;font-size:80px;line-height:1;color:var(--rose)}
</style>
</head>
<body>
<div class="page">

<header>
  <a class="brand" href="#">quill</a>
  <nav class="nav">
    <a href="#">HOME</a><a href="#">ABOUT US</a><a href="#">SUBMISSIONS</a><a href="#">PURCHASE</a><a href="#">CONTACT</a>
  </nav>
  <div class="social-top"><a href="#">Snapgram</a><a href="#">Facelog</a><a href="#">Chirper</a></div>
</header>

<section class="hero">
  <div class="block hero-bg"></div>
  <div class="block photo-tower" role="img" aria-label="Duotone purple photo of a tall building facade"></div>
  <div class="block photo-arches" role="img" aria-label="Duotone pink photo of a corridor of receding arches with steps"></div>
  <h1 class="abs hero-title">Quill is a plucky little publication out of Wellington, New Zealand</h1>
  <p class="abs hero-text">Quill is a literary and arts journal that provides a platform for both emerging and established writers and artists from New Zealand and beyond</p>
  <a class="btn" href="#" style="left:675px;top:544px;width:140px;height:52px">DONATE US</a>
</section>

<section class="competition">
  <div class="block comp-bg"></div>
  <h2 class="section-title centered" style="top:788px;font-size:38px">Annual short story competition</h2>
  <p class="abs comp-text">Issue One is interested in all that is spiritual, coincidental, or mysterious. Stories selected for this issue reflect life’s uncanny moments, those that defy explanation, and experiences that promote personal and spiritual growth. Entires must be no longer than 2000 words.</p>
  <div class="prize" style="left:349px">
    <svg width="34" height="38" viewBox="0 0 34 38" fill="none" stroke="#5e2753" stroke-width="1.6"><path d="M8 3h18v9a9 9 0 0 1-18 0z"/><path d="M8 6H3c0 6 3 8 6 8M26 6h5c0 6-3 8-6 8"/><path d="M17 21v8M10 35h14l-2-6H12z"/></svg>
    <div>First prize:<strong>1000</strong></div>
  </div>
  <div class="prize" style="left:540px">
    <svg width="34" height="38" viewBox="0 0 34 38" fill="none" stroke="#5e2753" stroke-width="1.6"><path d="M8 3h18v9a9 9 0 0 1-18 0z"/><path d="M8 6H3c0 6 3 8 6 8M26 6h5c0 6-3 8-6 8"/><path d="M17 21v8M10 35h14l-2-6H12z"/></svg>
    <div>Second prize:<strong>500</strong></div>
  </div>
  <div class="prize" style="left:721px">
    <svg width="34" height="38" viewBox="0 0 34 38" fill="none" stroke="#5e2753" stroke-width="1.6"><path d="M8 3h18v9a9 9 0 0 1-18 0z"/><path d="M8 6H3c0 6 3 8 6 8M26 6h5c0 6-3 8-6 8"/><path d="M17 21v8M10 35h14l-2-6H12z"/></svg>
    <div>Third prize:<strong>200 (EB3)</strong></div>
  </div>
</section>

<section class="about">
  <div class="block photo-leaves" role="img" aria-label="Dark moody photo of variegated leaves"></div>
  <div class="block photo-portrait" role="img" aria-label="Plum duotone portrait photo of a woman in glasses"></div>
  <h2 class="section-title" style="left:86px;top:1242px;font-size:38px">About Quill</h2>
  <p class="abs about-text">QUILL is an independent literary annual journal established in 2022 by Harriet Calloway and Mereana Platt that publishes unrepentant unfiltered accounts of life, eclectic takes on the mundane ordinary, and deep dives into modern love &amp; sexuality.</p>
  <p class="credit" style="top:1428px"><b>Founder, Editor</b>: Harriet Anahera Calloway</p>
  <p class="credit" style="top:1472px"><b>Founder, Production Director</b>: Mereana Platt</p>
  <p class="credit" style="top:1517px"><b>Art Direction</b>: Corin Ashby</p>
  <p class="credit" style="top:1561px"><b>Editorial Assistant</b>: Lucy Fenwick-Dorsey</p>
</section>

<section class="support">
  <div class="block photo-frame-leaf" role="img" aria-label="Pink photo of a monstera leaf through a gilt picture frame"></div>
  <div class="block photo-hand" role="img" aria-label="Pastel pink photo of a pointing hand in a red sleeve"></div>
  <h2 class="section-title" style="left:656px;top:1936px;font-size:46px">Support Us</h2>
  <p class="body-copy" style="left:656px;top:2014px;width:470px">Since our launch in 2022, we have relied upon the generous support of our creative business community in Wellington City, New Zealand. If you read us, or love our ethos, please consider a donation.</p>
  <a class="btn btn--rose" href="#" style="left:656px;top:2146px;width:138px;height:52px">GIVE A LITTLE</a>
</section>

<section class="submissions">
  <div class="block subm-bg"></div>
  <div class="block photo-monstera" role="img" aria-label="Violet and magenta duotone photo of a monstera leaf"></div>
  <h2 class="section-title" style="left:86px;top:2446px;width:470px;font-size:46px;line-height:52px">Quill welcomes submissions all year round.</h2>
  <p class="body-copy" style="left:86px;top:2620px;width:450px">We are drawn to dark humour, satirical takes on the social scene, and starkly honest accounts of ordinary life. Diversity is celebrated, adversity is welcomed and, above all, personal expression is championed. We are particularly seeking content that takes risks, screams of honesty and celebrates life’s most extraordinary moments.</p>
  <p class="body-copy" style="left:86px;top:2768px;width:450px">Selected works will be published in our annual publication.</p>
</section>

<section class="magazines">
  <div class="block mag-band"></div>
  <h2 class="section-title centered" style="top:3012px;font-size:50px">Our Upcoming Magazine</h2>
  <p class="abs" style="left:400px;top:3090px;width:400px;text-align:center;font-size:14px;line-height:22px;color:var(--muted)">Our back catalogue is available in digital format for a reduced price.</p>

  <article class="card" style="left:86px">
    <div class="card-head" style="background:#efe6d6;color:#6f6a22">
      <div class="card-meta"><span>ISSUE 001</span><span class="card-logo">quill</span><span>AUG 2022</span></div>
      <div class="card-img" style="background:linear-gradient(180deg,#8c8630,#6b6620)" role="img" aria-label="Olive duotone portrait photo"></div>
    </div>
    <h3 class="card-title">ISSUE 001 — AUG 2022</h3>
    <p class="card-text">Lorem ipsum dolor sit amet, consectetur adipiscing elit. Aenean dapibus</p>
    <a class="btn" href="#">DOWNLOAD NOW</a>
  </article>
  <article class="card" style="left:351px">
    <div class="card-head" style="background:#b54a6c;color:#f4d4de">
      <div class="card-meta"><span>ISSUE 002</span><span class="card-logo">quill</span><span>SEP 2022</span></div>
      <div class="card-img" style="background:linear-gradient(180deg,#8e3358,#6e2447)" role="img" aria-label="Rose duotone photo of a building facade"></div>
    </div>
    <h3 class="card-title">ISSUE 002 — SEP 2022</h3>
    <p class="card-text">Lorem ipsum dolor sit amet, consectetur adipiscing elit. Aenean dapibus</p>
    <a class="btn" href="#">DOWNLOAD NOW</a>
  </article>
  <article class="card" style="left:612px">
    <div class="card-head" style="background:#f1e6ef;color:#7a3b6e">
      <div class="card-meta"><span>ISSUE 003</span><span class="card-logo">quill</span><span>OCT 2022</span></div>
      <div class="card-img" style="background:linear-gradient(135deg,#1b1560,#6a2bb0 55%,#1a1250)" role="img" aria-label="Indigo duotone photo of a monstera leaf"></div>
    </div>
    <h3 class="card-title">ISSUE 003 — OCT 2022</h3>
    <p class="card-text">Lorem ipsum dolor sit amet, consectetur adipiscing elit. Aenean dapibus</p>
    <a class="btn" href="#">DOWNLOAD NOW</a>
  </article>
  <article class="card" style="left:876px">
    <div class="card-head" style="background:#6f7a2d;color:#e9c24a">
      <div class="card-meta"><span>ISSUE 004</span><span class="card-logo">quill</span><span>NOV 2022</span></div>
      <div class="card-img" style="background:linear-gradient(180deg,#e86aa8,#c94f8f)" role="img" aria-label="Pink duotone portrait photo"></div>
    </div>
    <h3 class="card-title">ISSUE 004 — NOV 2022</h3>
    <p class="card-text">Lorem ipsum dolor sit amet, consectetur adipiscing elit. Aenean dapibus</p>
    <a class="btn" href="#">DOWNLOAD NOW</a>
  </article>
  <div class="dots"><span></span><span></span><span></span><span></span></div>
</section>

<section class="newsletter">
  <h2 class="section-title centered" style="top:3880px;font-size:48px;line-height:53px">Subscribe to our weekly<br>newsletter</h2>
  <div class="block photo-blossom" role="img" aria-label="Lilac photo of a pink flowering sprig"></div>
  <div class="block news-card"></div>
  <p class="body-copy" style="left:519px;top:4140px;width:540px;font-size:13.5px;line-height:23px">Since our launch in 2022, we have relied upon the generous support of our creative business community in Wellington City, New Zealand. If you read us, or love our ethos, please consider a donation.</p>
  <div class="input">Email Address</div>
  <a class="btn-solid" href="#">SUBSCRIBE</a>
  <p class="abs" style="left:519px;top:4294px;font-size:13px;color:var(--ink)">We respect your privacy.</p>
</section>

<footer>
  <div class="block footer-bg"></div>
  <h3 class="foot-title" style="left:86px;top:4624px">Support Us</h3>
  <p class="body-copy" style="left:86px;top:4672px;width:330px;font-size:13.5px">Since our launch in 2022, we have relied upon the generous support of our creative business community in Wellington City, New Zealand. If you read us, or love our ethos, please consider a donation.</p>
  <a class="abs" href="#" style="left:86px;top:4814px;display:flex;align-items:center;gap:12px;font-family:var(--cond);font-size:18px;color:var(--ink)">GIVE A LITTLE
    <svg width="24" height="12" viewBox="0 0 24 12" fill="none" stroke="#3b3340" stroke-width="1.6"><path d="M0 6h22M17 1l5 5-5 5"/></svg></a>
  <h3 class="foot-title" style="left:561px;top:4626px">Main Menu</h3>
  <div class="foot-links" style="left:561px;top:4674px"><a href="#">Home</a><br><a href="#">About</a><br><a href="#">Submissions</a><br><a href="#">Purchase</a><br><a href="#">Contact</a></div>
  <h3 class="foot-title" style="left:777px;top:4626px">Social</h3>
  <div class="foot-links foot-links--u" style="left:777px;top:4674px"><a href="#">Facelog</a><br><a href="#">Snapgram</a><br><a href="#">Chirper</a></div>
  <span class="foot-brand">quill</span>
  <p class="abs" style="left:943px;top:4736px;font-size:14px;color:var(--ink)">Made with <a href="#" style="color:var(--rose);text-decoration:underline">Sitecraft</a></p>
</footer>

</div>
</body>
</html>
```